PowerPoint template for online medical education

Need a PowerPoint design for our online urgent care education content Need a title page and then further pages.

must have our logo, name and tagline Academy of Rapid Clinical Practice
Inspiring excellence, Advancing the specialty
Should match our logo colors scheme

enclosed our logo, tagline ans a copy of our newsletter

Target Market(s)

PHYSICIANS, and other professionals

Industry/Entity Type

Medicine

Font styles to use
Serif

Requirements
Must have
• our logo
• tagline
• color scheme like our logo
Should not have
• too much on content pages

```html
<!DOCTYPE html>
<html lang="en">
<head>
<meta charset="utf-8">
<title>Academy of Rapid Clinical Practice – Presentation Template</title>
<link href="https://fonts.googleapis.com/css2?family=Archivo+Black&family=Arimo:ital,wght@0,400;0,700;1,700&display=swap" rel="stylesheet">
<style>
  :root{
    --board:#625e5c;
    --paper:#ffffff;
    --orange:#f2a541;
    --red:#b8402c;
    --ink:#231f20;
    --text:#4a4a4a;
    --muted:#6d6e71;
  }
  *{box-sizing:border-box;margin:0;padding:0}
  html,body{width:1200px;height:1200px;overflow:hidden;background:var(--board)}
  body{position:relative;font-family:"Arimo",Arial,sans-serif;color:var(--text)}

  .slide{position:absolute;width:438px;height:339px;background:var(--paper);overflow:hidden}
  .slide--title{left:84px;top:62px}
  .slide--editor{left:676px;top:63px;width:434px;height:335px}
  .slide--cover{left:86px;top:432px;width:437px;height:338px}
  .slide--literature{left:674px;top:434px;width:437px;height:338px}
  .slide--president{left:83px;top:806px}
  .slide--cases{left:673px;top:809px}

  .band-top{position:absolute;left:0;top:0;right:0;height:20px;background:var(--orange)}
  .band-bottom{position:absolute;left:0;right:0;bottom:0;height:16px;
    background:linear-gradient(115deg,var(--orange) 0,var(--orange) 61.5%,var(--paper) 61.5%,var(--paper) 62.3%,var(--red) 62.3%)}
  .band-bottom__label{position:absolute;left:29px;top:3px;font-size:9.5px;font-weight:700;color:#fff;letter-spacing:.2px}

  .wordmark{position:absolute;display:flex;align-items:center}
  .wordmark__dot{border-radius:50%;background:var(--orange);flex:none}
  .wordmark__name{font-weight:400;color:var(--muted);font-variant:small-caps;letter-spacing:1.5px}
  .wordmark--large{left:74px;top:122px}
  .wordmark--large .wordmark__dot{width:64px;height:64px;margin-right:40px}
  .wordmark--large .wordmark__name{font-size:27px;line-height:28px}
  .wordmark--small{left:134px;top:168px}
  .wordmark--small .wordmark__dot{width:38px;height:38px;margin-right:22px}
  .wordmark--small .wordmark__name{font-size:16.5px;line-height:17.5px}

  .tagline{position:absolute;left:186px;top:246px;font-size:9.5px;font-weight:700;font-style:italic;color:var(--red)}

  .cover-title{position:absolute;left:0;right:0;top:84px;text-align:center;font-family:"Archivo Black","Arimo",sans-serif;font-size:36px;color:var(--ink);letter-spacing:.5px}

  .photo{position:absolute;left:36px;top:47px;width:118px;height:125px}
  .photo--editor{background:linear-gradient(180deg,#4f4d49 0%,#7d766d 45%,#3b3b3d 100%)}
  .photo--literature{background:linear-gradient(180deg,#d9d6d2 0%,#8a5b45 45%,#eeeeee 100%)}
  .photo--president{background:linear-gradient(180deg,#585e66 0%,#a07c63 45%,#6a87a8 100%)}
  .photo--cases{background:linear-gradient(180deg,#6b241c 0%,#c79a6e 50%,#f1ece6 100%)}

  .nametag{position:absolute;left:0;height:15px;width:154px;
    background:linear-gradient(115deg,var(--orange) 0,var(--orange) 79%,var(--paper) 79%,var(--paper) 80.5%,var(--red) 80.5%)}
  .nametag__name{position:absolute;left:38px;top:3.5px;font-size:7px;font-weight:700;color:#fff;white-space:nowrap}
  .role{position:absolute;left:38px;font-size:8px;font-weight:700;color:var(--text);white-space:nowrap}

  .article{position:absolute;left:166px;width:244px}
  .article__kicker{font-size:7.8px;font-weight:700;color:var(--text);letter-spacing:.2px}
  .article__title{font-size:7.8px;font-weight:700;color:var(--ink);margin-bottom:6px}
  .article p{font-size:5.6px;line-height:7.3px;text-align:justify;color:var(--text)}
  .article .gap{margin-top:6px}
  .contact{position:absolute;right:30px;top:203px;font-size:6.2px;color:var(--text)}
</style>
</head>
<body>

<section class="slide slide--title">
  <div class="band-top"></div>
  <div class="wordmark wordmark--large">
    <span class="wordmark__dot"></span>
    <span class="wordmark__name">Academy of<br>Rapid Clinical<br>Practice</span>
  </div>
  <p class="tagline">Inspiring Exellence, Advancing the Specialty</p>
  <div class="band-bottom"></div>
</section>

<section class="slide slide--editor">
  <div class="band-top"></div>
  <div class="photo photo--editor" style="top:59px" role="img" aria-label="Portrait photo of the newsletter editor"></div>
  <div class="nametag" style="top:184px"><span class="nametag__name">Daniel Whitcombe, MD</span></div>
  <p class="role" style="top:202px">EDITOR'S CORNER</p>
  <div class="article" style="top:49px;width:242px">
    <p class="article__title">TO LEAD OR FOLLOW: THAT IS THE QUESTION</p>
    <p>Year two of Rapid Rounds is here. This year we plan to be bigger, better and full of news and information for clinicians who work in the on demand space. As our president, Dr Malhotra, has explained the Academy has ambitious goals to make life easier for us providers and our patients.</p>
    <p>There are many challenges for our specialty now and we expect more into the future. Others are making decisions about how we care for our patients and the future of this specialty. We have two choices: lead or follow. The academy plans to lead.</p>
    <p class="gap">Where do you stand? If you wish to lead, you can face these challenges alone or as part of ARCP. Individually you can make changes, but as a group we can do so much more. Join ARCP today. The more providers we represent, the greater our influence. Send in a case or an article for this newsletter. Join a committee. Even decide to run for the board this fall. Every little bit counts.</p>
  </div>
  <p class="contact">Contact Dr. Daniel Whitcombe: dwhitcombe@arcp-mail.org</p>
  <div class="band-bottom"><span class="band-bottom__label">ACADEMY OF RAPID CLINICAL PRACTICE</span></div>
</section>

<section class="slide slide--cover">
  <div class="band-top"></div>
  <h1 class="cover-title">RAPID ROUNDS</h1>
  <div class="wordmark wordmark--small">
    <span class="wordmark__dot"></span>
    <span class="wordmark__name">Academy of<br>Rapid Clinical<br>Practice</span>
  </div>
  <div class="band-bottom"></div>
</section>

<section class="slide slide--literature">
  <div class="band-top"></div>
  <div class="photo photo--literature" style="top:47px" role="img" aria-label="Portrait photo of the article author in a white coat"></div>
  <div class="nametag" style="top:172px"></div>
  <div class="article" style="top:48px">
    <p class="article__kicker">NEW IN THE LITERATURE</p>
    <p class="article__title">Part 1: HBTI, New Blood Test for Concussion</p>
    <p>On February 14, 2018, the National Health Products Agency (NHPA) approved marketing of the first blood test to evaluate the need of computed tomography (CT) in patients with mild traumatic brain injury (mTBI). The Harbor Brain Trauma Indicator (HBTI), by Harbor Biomarkers in San Diego.</p>
    <p>“Availability of a blood test for concussion will help health care professionals determine the need for a CT scan in patients suspected of having mTBI and help prevent unnecessary neuroimaging and associated radiation exposure to patients.” An agency initiative was set to decrease exposure to unnecessary radiation and the HBTI fits into it nicely, passing in only 6 months. The defense research office performed 2,000 blood tests leading to the approval of the HBTI. The HBTI measures two proteins that are released into the bloodstream after a mild TBI. The two proteins are ubiquitin C-terminal hydrolase (UCH-L1) and glial fibrillary acidic protein (GFAP). GFAP is a protein expressed by astrocytes and UCH-L1 is expressed by neurons. When a head injury occurs, these two proteins are leaked from the cells and enter the bloodstream. Both are detectable within one hour after mTBI. UCH-L1 rises rapidly, peaking at 8 hours. While GFAP rises slowly, peaking at 20 hours and declining over the following 72 hours. Currently, the standard of care after head trauma is for the clinician to perform a neurological evaluation and CT scan, if indicated. The proposed utility of the test is to avoid unnecessary CT scans. The HBTI proteins are detectable by a point of care (POC) test approximately 12 hours after a head trauma. The test is approved for use in adults only currently.</p>
    <p>The test leaves many questions, what will the patient demand me? Will it change our management after normal neurological exams? What will be the price and utility for the standard urgent care center? Will this testing be available to non-clinicians in sports or battlefields? We will look at these questions in Part 2 of the series HBTI Testing.</p>
    <p>NHPA. Agency authorizes marketing of first blood test to aid in the evaluation of concussion in adults. NHPA News Release. February 14, 2018. Retrieved from https://www.nhpa-news.org/press/</p>
    <p>Harbor Biomarkers, 2018. Developing the First Objective Blood Test for Traumatic Brain Injury. Retrieved from https://harborbio-labs.com/</p>
  </div>
  <div class="band-bottom"><span class="band-bottom__label">ACADEMY OF RAPID CLINICAL PRACTICE</span></div>
</section>

<section class="slide slide--president">
  <div class="band-top"></div>
  <div class="photo photo--president" style="top:49px;left:37px" role="img" aria-label="Portrait photo of the academy president wearing a stethoscope"></div>
  <div class="nametag" style="top:173px"><span class="nametag__name">Arjun Malhotra, MD</span></div>
  <p class="role" style="top:195px">ARCP PRESIDENT</p>
  <div class="article" style="top:50px;left:167px;width:243px">
    <p>Urgent care clinicians all over the country are working hard to provide the highest quality care to their patients and communities. As the needs of every patient differ, the goal that needs to be set for each patient can differ as well. Our vision, however, is something that has to be common….it needs to be aligned. Antibiotic stewardship is an important aspect of what the current focus is within the Academy. Our vision is to see urgent care clinicians be the champions of antibiotic stewardship and lead this change nationally.</p>
    <p class="gap">The National Disease Institute estimates that in outpatient settings, 30 percent of all antibiotics prescribed in outpatient clinics are unnecessary. Even when antibiotics are needed, prescribers often favor drugs that may be less effective and carry more risk over more targeted first-line drugs recommended by national guidelines. Given that there are currently more than nine thousand urgent care clinics within United States and more opening at a rapid pace, these statistics become relevant to us as a clinician community. We need to ask ourselves some questions: Are we communicating enough as a group of clinicians? Are we discussing this issue frequently enough amongst ourselves? How do we engage our peers to be the champions of antibiotic stewardship? How do we engage patients to be advocates for antibiotic stewardship? What information, data and/or education do the urgent care clinicians need in order to develop strategies that will help better navigate the troubled waters of excess antibiotic use? Within our clinics, and in our communities, are we doing enough to raise awareness regarding this important issue? And many more such questions.</p>
    <p class="gap">As the Academy's Antibiotic Stewardship Committee continues to work on this issue, nothing would give us more pleasure than to see our members getting more involved and engaged in this discussion. Our doors are always open for our members to join in these discussions and be part of these committees. We are confident that vision aligns well with that of our members.</p>
    <p class="gap">If you are interested in being part of the committees, please contact me at arjun.malhotra@arcp-mail.org. I look forward to hearing from you.</p>
  </div>
  <div class="band-bottom"><span class="band-bottom__label">ACADEMY OF RAPID CLINICAL PRACTICE</span></div>
</section>

<section class="slide slide--cases">
  <div class="band-top"></div>
  <div class="photo photo--cases" style="top:49px;left:37px;height:126px" role="img" aria-label="Portrait photo of the case author, a board member"></div>
  <div class="nametag" style="top:175px"><span class="nametag__name">Lena Marsh, MBA, PA-C</span></div>
  <p class="role" style="top:196px;font-size:7.5px">Member of the ARCP board HPI</p>
  <div class="article" style="top:49px;width:246px">
    <p class="article__kicker">CASES FROM OUR MEMBERS</p>
    <p class="article__title">A worrisome rash</p>
    <p>Lena Marsh, MBA, PA-C is a member of the ARCP board</p>
    <p>HPI: This is a 34 yo healthy female with no past medical history who presents complaining of a rash on the bilateral upper and lower extremities x 2 weeks. She states that red spots first started on her bilateral lower legs 2 weeks ago, after no known new exposures or illness. She was seen at urgent care and it was believed that she had spider bites as there was a central papule in each lesion, she was started on TMP-SMX DS BID. The rash progressed up the lower extremities and then started to appear on the upper extremities yesterday. Patient notes that the rash on her arms appears more like hives and she began to experience joint pain in her left ankle to the point where she has difficulty walking. She reports the lesions start with a burning sensation in the skin and then the color appears a day later. No other joint swelling. Rash spares the trunk. No mouth lesions. She also states she has a few random areas of bruising on her thighs.</p>
    <p>PE: Afebrile, vitals stable. Examination of the rash on the bilateral forearms reveals urticarial wheals in no particular pattern. The rash stops at the elbows. Examination of the bilateral lower extremities reveals non-blanching petechial macules, no vesicles. No involvement of the nails. The left ankle is very tender with ROM but no asymmetrical swelling noted. Diagnosis: Suspect Urticarial Vasculitis, no biopsy was performed at time of visit.</p>
  </div>
  <div class="band-bottom"></div>
</section>

</body>
</html>
```